Web Page Design for a Website that Provides Tutoring

I am looking to create an online tutoring website. The website will allow parents or students to contact tutors with a view to instructing them to tutor themselves or their children.

The name of the website is LendYourLessons.

This brief is to create the design for one of the web pages for this web site. I am hoping the same designer will be available to design other pages.

The page I want designed is one of the more complex and I have attached the design as an excel spreadsheet. The web page needs to include all the items on this page but if you want to change the positioning of the items then Im fine with that.

I recently had two logos created for this website. My favourite is the one with a mortar board but im not sure I like the colours. I have attached both of these logos and you can use either of them, change the colours or create something different. I just want a design pleasing to the eye. If the logo is changed I would like that in a seperate file.

So can you please submit designs for this page. I have attached the two logos which you can use, change or if you feel you have a better idea then you can use that.

On the spreadsheet the Send Message, Favourite etc are buttons.

Target Market(s)

People who want to better themselves.
Possible middle class to upper class.

Industry/Entity Type

Tutoring

Number of Pages Required

1 page

Requirements
Must have
• The designs must have alot of the information attached in the spreadsheet.

```html
<!DOCTYPE html>
<html lang="en">
<head>
<meta charset="utf-8">
<title>LendYourLessons – Online Tutoring</title>
<link href="https://fonts.googleapis.com/css2?family=Open+Sans:ital,wght@0,400;0,600;0,700;0,800;1,400;1,600&display=swap" rel="stylesheet">
<style>
:root{
  --navy:#0f2b52;
  --navy-deep:#0b2242;
  --orange:#f26640;
  --yellow:#f7d53f;
  --blue-star:#2f63c4;
  --grey-bg:#ececec;
  --text:#444;
  --muted:#888;
  --white:#fff;
  --footer:#1c1c1c;
  --footer-base:#111;
}
*{box-sizing:border-box;margin:0;padding:0}
html,body{width:1200px;height:4255px;overflow:hidden}
body{font-family:"Open Sans",Arial,sans-serif;color:var(--text);background:var(--white);position:relative}
.section{position:relative;width:1200px}
.wrap{position:absolute;left:85px;width:1030px}

/* header */
.hero{height:743px;background:linear-gradient(180deg,#7f93a8 0%,#a7b4c0 45%,#c9c3b8 100%)}
.hero-photo{position:absolute;inset:0;background:linear-gradient(100deg,#6f86a0 0%,#a4b0bd 40%,#d8c6ad 60%,#9fb0c0 100%)}
.hero-shade{position:absolute;inset:0;background:rgba(20,45,80,.35)}
.topbar{position:absolute;top:0;left:0;width:1200px;height:40px;background:var(--navy-deep);display:flex;justify-content:flex-end;align-items:center;gap:26px;padding-right:85px;color:#cfd8e6;font-size:12px}
.topbar span{display:flex;align-items:center;gap:7px}
.navbar{position:absolute;top:40px;left:0;width:1200px;height:96px;background:rgba(15,43,82,.92)}
.brand{position:absolute;left:85px;top:22px;display:flex;align-items:center;gap:10px;color:var(--white);font-weight:700;font-size:22px}
.brand-mark{width:40px;height:40px;background:var(--orange)}
.nav{position:absolute;right:85px;top:34px;display:flex;gap:34px;align-items:center;color:var(--white);font-weight:700;font-size:15px}
.hero-arrow{position:absolute;top:420px}
.hero-title{position:absolute;top:375px;width:1200px;text-align:center;color:var(--white);font-size:64px;font-weight:600;letter-spacing:1px}
.hero-sub{position:absolute;top:444px;left:300px;width:600px;text-align:center;color:var(--white);font-style:italic;font-weight:600;font-size:15px;line-height:23px}
.tabs{position:absolute;top:504px;left:425px;display:flex}
.tab{width:174px;height:36px;display:flex;align-items:center;justify-content:center;color:var(--white);font-size:14px;font-weight:600;background:#5b6470}
.tab.active{background:var(--orange)}
.search{position:absolute;top:542px;left:318px;width:562px;height:105px;background:rgba(255,255,255,.35);padding:12px 15px}
.field{position:absolute;background:var(--white);height:36px;font-size:13px;color:#999;padding:0 14px;display:flex;align-items:center;justify-content:space-between}
.search-btn{position:absolute;right:15px;top:12px;width:85px;height:81px;background:var(--orange);display:flex;align-items:center;justify-content:center}

/* shared headings */
.heading{position:absolute;display:flex;align-items:center;gap:10px}
.heading .mark{width:34px;height:34px;background:var(--orange)}
.heading h2{font-size:29px;font-weight:700;color:var(--navy)}
.heading .rule{width:100px;height:2px;background:var(--orange);margin-left:8px;margin-top:12px}
.heading-sub{position:absolute;font-style:italic;font-weight:600;font-size:14px;color:#555}

/* welcome */
.welcome{height:463px}
.intro{position:absolute;top:170px;font-size:14px;line-height:23px;color:var(--text)}
.stat{position:absolute;top:270px;height:113px;display:flex;align-items:center;gap:28px}
.stat-score{left:0;width:335px;background:var(--orange);padding-left:30px;color:var(--white)}
.stat h3{font-style:italic;font-weight:600;font-size:20px;margin-bottom:4px}
.stat .divider{position:absolute;width:4px;height:113px;background:var(--orange)}
.stars{display:flex;gap:3px}

/* how it works */
.how{height:488px;background:var(--grey-bg)}
.step{position:absolute;top:178px;width:270px;text-align:center}
.step .ico{height:90px;display:flex;justify-content:center;align-items:center}
.step h4{font-size:15px;font-weight:600;color:#222;margin-top:14px;line-height:19px}
.step p{font-size:13px;color:var(--muted);line-height:19px;margin-top:10px}
.step a{display:block;margin-top:12px;color:var(--orange);font-size:13px;font-weight:600;text-decoration:none}

/* tutors */
.tutors{height:547px}
.tutor{position:absolute;top:153px;width:247px;height:301px;background:var(--yellow);border:3px solid var(--navy)}
.tutor.highlight{background:var(--navy);border-color:var(--navy)}
.tutor .photo{position:absolute;top:8px;left:8px;width:225px;height:135px;background:linear-gradient(180deg,#e8eef5,#c9d4df);border:6px solid var(--navy)}
.tutor.highlight .photo{border-color:var(--yellow);background:linear-gradient(180deg,#f6d45a,#e8bb3b)}
.tutor-info{position:absolute;top:168px;width:100%;text-align:center;padding:0 16px}
.tutor-info h4{font-size:15px;font-weight:700;color:#222}
.tutor-info small{display:block;font-size:11px;color:#333;margin:2px 0 6px}
.tutor-info p{font-size:12px;line-height:17px;color:#333}
.tutor.highlight .tutor-info h4,.tutor.highlight .tutor-info small,.tutor.highlight .tutor-info p{color:var(--white)}
.tutor .stars{justify-content:center;margin-top:10px}
.register{position:absolute;left:50px;top:50px;width:125px;height:28px;border:2px solid var(--white);color:var(--white);font-size:12px;font-weight:700;display:flex;align-items:center;justify-content:center}
.socials{position:absolute;left:84px;top:88px;display:flex;gap:10px}
.socials i{width:14px;height:14px;background:var(--white);display:block}

/* students */
.students{height:468px;background:var(--navy)}
.students-photo{position:absolute;left:0;top:0;width:600px;height:468px;background:linear-gradient(135deg,#3c2a22 0%,#8a5a3a 40%,#c48a52 65%,#5a4030 100%)}
.student-list{position:absolute;left:667px;top:150px;width:450px}
.student{display:flex;gap:14px;margin-bottom:13px}
.student .avatar{width:46px;height:46px;border:2px solid var(--white);background:linear-gradient(135deg,#8d6b4c,#c9a27a);flex:none}
.student h5{font-style:italic;font-weight:600;font-size:14px;color:var(--white)}
.student p{font-size:12.5px;line-height:17px;color:#d8e0ea}
.btn-yellow{position:absolute;left:667px;top:363px;width:178px;height:34px;background:var(--yellow);color:var(--navy);font-size:13px;font-weight:700;display:flex;align-items:center;justify-content:center}

/* courses */
.courses{height:474px}
.course{position:absolute;top:162px;width:241px}
.course .photo{height:179px}
.course h4{font-size:15px;font-weight:600;color:#222;margin-top:20px}
.course .meta{display:flex;gap:18px;align-items:center;font-size:12px;color:var(--muted);margin-top:10px}
.course .price{margin-left:auto;color:var(--orange);font-weight:700}

/* counters */
.counters{height:159px;background:var(--orange)}
.counter{position:absolute;top:30px;display:flex;align-items:center;gap:14px;color:var(--white)}
.counter b{font-size:88px;font-weight:400;line-height:100px}
.counter span{font-size:13px;font-weight:700;line-height:17px;text-transform:uppercase}

/* news */
.news{height:559px}
.post{position:absolute;top:170px;width:323px}
.post .photo{position:relative;height:171px}
.date{position:absolute;left:0;bottom:0;width:58px;height:60px;background:var(--orange);color:var(--white);text-align:center;font-weight:700;font-size:16px;line-height:22px;padding-top:8px}
.post .by{font-size:12px;font-style:italic;color:var(--muted);margin-top:22px;display:flex;gap:40px}
.post h4{font-size:15px;font-weight:600;color:#222;line-height:21px;margin-top:6px}
.post p{font-size:12.5px;line-height:18px;color:var(--muted);margin-top:8px}

/* footer */
.footer{height:298px;background:var(--footer)}
.footer .brand{top:70px;left:85px;font-size:21px}
.footer-about{position:absolute;left:85px;top:130px;width:245px;font-size:12px;line-height:18px;color:#bbb}
.footer-social{position:absolute;left:85px;top:240px;display:flex;gap:12px}
.footer-social i{width:28px;height:28px;background:#aaa;display:block}
.fcol{position:absolute;top:80px;color:#ccc;font-size:13px;line-height:22px}
.fcol h5{font-style:italic;font-weight:600;font-size:14px;color:var(--white);border-bottom:2px solid var(--orange);padding-bottom:4px;margin-bottom:8px;display:inline-block}
.fcol li{list-style:none}
.contact li{display:flex;gap:10px;margin-bottom:10px;line-height:18px}
.base{height:56px;background:var(--footer-base);color:#888;font-size:12px;display:flex;align-items:center;justify-content:center}
</style>
</head>
<body>

<header class="section hero">
  <div class="hero-photo" role="img" aria-label="Photo of a tutor helping a young student study at a desk"></div>
  <div class="hero-shade"></div>
  <div class="topbar">
    <span><svg width="12" height="12" viewBox="0 0 12 12"><circle cx="6" cy="6" r="5" fill="none" stroke="#cfd8e6" stroke-width="1.5"/><path d="M6 3v3h2" stroke="#cfd8e6" stroke-width="1.5" fill="none"/></svg>MON - FRI : 9.00AM - 06.00PM</span>
    <span><svg width="12" height="12" viewBox="0 0 12 12"><path d="M2 1l3 1-1 3 3 3 3-1 1 3-2 1C5 11 1 7 1 3z" fill="#cfd8e6"/></svg>+1-555-010-2040</span>
    <span>Register&nbsp;&nbsp;|&nbsp;&nbsp;Login</span>
  </div>
  <nav class="navbar">
    <div class="brand"><span class="brand-mark"></span>LendYourLessons</div>
    <div class="nav">
      <span>HOME</span><span>STUDENT</span><span>TUTOR</span><span>ABOUT</span><span>CONTACT</span>
      <svg width="26" height="26" viewBox="0 0 26 26"><circle cx="11" cy="11" r="8" fill="none" stroke="#fff" stroke-width="3"/><path d="M17 17l7 7" stroke="#fff" stroke-width="3.5"/></svg>
    </div>
  </nav>
  <svg class="hero-arrow" style="left:62px" width="24" height="44" viewBox="0 0 24 44"><path d="M20 4L4 22l16 18" stroke="#fff" stroke-width="2" fill="none"/></svg>
  <svg class="hero-arrow" style="left:1114px" width="24" height="44" viewBox="0 0 24 44"><path d="M4 4l16 18L4 40" stroke="#fff" stroke-width="2" fill="none"/></svg>
  <h1 class="hero-title">LEND YOUR LESSONS</h1>
  <p class="hero-sub">Lorem ipsum dolor sit amet, consectetur adipiscing elit. Phasellus molestie lorem vitae velit con sect tur malesuada. Phasellus velit mauris, commodo at tincidunt et</p>
  <div class="tabs"><span class="tab active">TEACHER</span><span class="tab">STUDENT</span></div>
  <div class="search">
    <div class="field" style="left:15px;top:12px;width:435px">Find a Teacher</div>
    <div class="field" style="left:15px;top:57px;width:215px">Select Subject <svg width="10" height="6"><path d="M0 0h10L5 6z" fill="#555"/></svg></div>
    <div class="field" style="left:237px;top:57px;width:213px">Postcode</div>
    <div class="search-btn"><svg width="34" height="34" viewBox="0 0 34 34"><circle cx="14" cy="14" r="10" fill="none" stroke="#fff" stroke-width="4"/><path d="M21 21l10 10" stroke="#fff" stroke-width="5"/></svg></div>
  </div>
</header>

<section class="section welcome">
  <div class="wrap">
    <div class="heading" style="top:92px"><span class="mark"></span><h2>Welcome To Lend Your Lessons</h2><span class="rule"></span></div>
    <p class="heading-sub" style="top:128px">vehicula ipsum sagittis vitae</p>
    <p class="intro">Lorem ipsum dolor sit amet, consectetur adipiscing elit. Phasellus molestie lorem vitae velit consectetur malesuada. Phasellus velit mauriscо mmodo at tincidunt et, dapibus ullamcorper sapien. Donec rhoncus congue congue. Aliquam in lorem sagittis, rutrum libero sit amet, tempus lacus. Cum sociis natoque penatibus et magnis dis parturient montes.Lorem ipsum dolor</p>
    <div class="stat stat-score">
      <svg width="64" height="64" viewBox="0 0 64 64"><circle cx="32" cy="32" r="26" fill="none" stroke="#fff" stroke-width="3" stroke-dasharray="120 20"/><circle cx="32" cy="27" r="7" fill="none" stroke="#fff" stroke-width="3"/><path d="M20 44c4-8 20-8 24 0" fill="none" stroke="#fff" stroke-width="3"/></svg>
      <div><h3>Review Score</h3>
        <div class="stars"><svg width="110" height="20" viewBox="0 0 110 20"><g fill="#fff"><path id="s1" d="M10 1l2.6 6 6.4.5-4.9 4.2 1.5 6.3L10 14.6 4.4 18l1.5-6.3L1 7.5l6.4-.5z"/><use href="#s1" x="22"/><use href="#s1" x="44"/><use href="#s1" x="66"/><use href="#s1" x="88"/></g></svg></div></div>
    </div>
    <span class="stat divider" style="left:355px;top:270px"></span>
    <div class="stat" style="left:400px">
      <svg width="70" height="70" viewBox="0 0 70 70"><circle cx="35" cy="35" r="30" fill="none" stroke="#123" stroke-width="4"/><path d="M20 35l11 11 20-22" fill="none" stroke="#123" stroke-width="5"/></svg>
      <div><h3 style="color:var(--orange)">Reliability</h3>
        <svg width="130" height="22" viewBox="0 0 130 22"><g fill="#2f63c4"><use href="#s1"/><use href="#s1" x="25"/><use href="#s1" x="50"/><use href="#s1" x="75"/><use href="#s1" x="100" opacity=".5"/></g></svg></div>
    </div>
    <span class="stat divider" style="left:704px;top:270px"></span>
    <div class="stat" style="left:750px">
      <svg width="70" height="70" viewBox="0 0 70 70"><circle cx="35" cy="35" r="30" fill="none" stroke="#123" stroke-width="4" stroke-dasharray="160 30"/><path d="M35 16v19h14" fill="none" stroke="#123" stroke-width="5"/></svg>
      <div><h3 style="color:var(--orange)">Punctuality</h3>
        <svg width="130" height="22" viewBox="0 0 130 22"><g fill="#2f63c4"><use href="#s1"/><use href="#s1" x="25"/><use href="#s1" x="50"/><use href="#s1" x="75"/><use href="#s1" x="100" opacity=".5"/></g></svg></div>
    </div>
  </div>
</section>

<section class="section how">
  <div class="wrap">
    <div class="heading" style="top:78px"><span class="mark"></span><h2>How It Works</h2><span class="rule"></span></div>
    <p class="heading-sub" style="top:114px">vehicula ipsum sagittis vitae</p>
    <div class="step" style="left:-33px">
      <div class="ico"><svg width="70" height="90" viewBox="0 0 70 90"><circle cx="35" cy="20" r="15" fill="#2d6b2d"/><path d="M8 88V58c0-12 10-20 27-20s27 8 27 20v30z" fill="#2d6b2d"/><path d="M35 40v30" stroke="#fff" stroke-width="3"/></svg></div>
      <h4>Select<br>Your Private Tutor</h4>
      <p>Lorem ipsum dolor sit amet, con sectetur adipiscing elit. Aenean odio lorem porta.</p><a>Read More</a>
    </div>
    <div class="step" style="left:242px">
      <div class="ico"><svg width="90" height="90" viewBox="0 0 90 90"><circle cx="30" cy="32" r="13" fill="#2d6b2d"/><path d="M6 88V66c0-12 10-18 24-18s24 6 24 18v22z" fill="#2d6b2d"/><rect x="50" y="4" width="36" height="22" rx="3" fill="#2d6b2d"/><path d="M56 26l-4 8 10-8z" fill="#2d6b2d"/><g fill="#fff"><circle cx="60" cy="15" r="2.5"/><circle cx="68" cy="15" r="2.5"/><circle cx="76" cy="15" r="2.5"/></g></svg></div>
      <h4>Discuss your<br>educational needs</h4>
      <p>Lorem ipsum dolor sit amet, con sectetur adipiscing elit. Aenean odio lorem porta.</p><a>Read More</a>
    </div>
    <div class="step" style="left:523px">
      <div class="ico"><svg width="90" height="90" viewBox="0 0 90 90"><circle cx="45" cy="50" r="34" fill="none" stroke="#2d6b2d" stroke-width="4"/><path d="M11 50h68M45 16v68M20 30h50M20 70h50" stroke="#2d6b2d" stroke-width="3"/><path d="M45 4L84 18 45 32 6 18z" fill="#2d6b2d"/></svg></div>
      <h4 style="margin-top:24px">Start learning</h4>
      <p>Lorem ipsum dolor sit amet, con sectetur adipiscing elit. Aenean odio lorem porta.</p><a>Read More</a>
    </div>
    <div class="step" style="left:790px">
      <div class="ico"><svg width="90" height="80" viewBox="0 0 90 80"><rect x="10" y="6" width="70" height="48" rx="4" fill="none" stroke="#2d6b2d" stroke-width="5"/><path d="M2 62h86l-6 12H8z" fill="#2d6b2d"/><circle cx="45" cy="30" r="12" fill="none" stroke="#2d6b2d" stroke-width="3"/><path d="M45 22v8h6" stroke="#2d6b2d" stroke-width="3" fill="none"/></svg></div>
      <h4 style="margin-top:24px">Availability</h4>
      <p>Lorem ipsum dolor sit amet, con sectetur adipiscing elit. Aenean odio lorem porta.</p><a>Read More</a>
    </div>
  </div>
</section>

<section class="section tutors">
  <div class="wrap">
    <div class="heading" style="top:80px"><span class="mark"></span><h2>Our Favourite Tutors</h2><span class="rule"></span></div>
    <p class="heading-sub" style="top:116px">vehicula ipsum sagittis vitae</p>
    <div class="tutor highlight" style="left:0">
      <div class="photo" role="img" aria-label="Tutor portrait with register overlay"><span class="register">REGISTER</span><span class="socials"><i></i><i></i><i></i></span></div>
      <div class="tutor-info"><h4>CSECTETUR APISCING</h4><small>DONEFRINGILLA</small><p>Lorem ipsum dolor sit amet, con sectetur adipiscing elit. Aenean odio lorem.</p>
        <div class="stars"><svg width="100" height="18" viewBox="0 0 110 20"><g fill="#fff"><use href="#s1"/><use href="#s1" x="22"/><use href="#s1" x="44"/><use href="#s1" x="66"/><use href="#s1" x="88"/></g></svg></div></div>
    </div>
    <div class="tutor" style="left:261px">
      <div class="photo" role="img" aria-label="Portrait of a tutor in shirt and tie"></div>
      <div class="tutor-info"><h4>SECTETUR APISCING</h4><small>DONEFRINGILLA</small><p>Lorem ipsum dolor sit amet, con sectetur adipiscing elit. Aenean odio lorem.</p>
        <div class="stars"><svg width="100" height="18" viewBox="0 0 110 20"><g fill="#222"><use href="#s1"/><use href="#s1" x="22"/><use href="#s1" x="44"/><use href="#s1" x="66"/><use href="#s1" x="88" opacity=".4"/></g></svg></div></div>
    </div>
    <div class="tutor" style="left:522px">
      <div class="photo" role="img" aria-label="Portrait of a tutor in shirt and tie"></div>
      <div class="tutor-info"><h4>TURCSECTE APISCING</h4><small>DONEFRINGILLA</small><p>Lorem ipsum dolor sit amet, con sectetur adipiscing elit. Aenean odio lorem.</p>
        <div class="stars"><svg width="100" height="18" viewBox="0 0 110 20"><g fill="#222"><use href="#s1"/><use href="#s1" x="22"/><use href="#s1" x="44"/><use href="#s1" x="66"/><use href="#s1" x="88" opacity=".4"/></g></svg></div></div>
    </div>
    <div class="tutor" style="left:783px">
      <div class="photo" role="img" aria-label="Portrait of a tutor in shirt and tie"></div>
      <div class="tutor-info"><h4>URCSECTET APISCING</h4><small>DONEFRINGILLA</small><p>Lorem ipsum dolor sit amet, con sectetur adipiscing elit. Aenean odio lorem.</p>
        <div class="stars"><svg width="100" height="18" viewBox="0 0 110 20"><g fill="#222"><use href="#s1"/><use href="#s1" x="22"/><use href="#s1" x="44"/><use href="#s1" x="66"/><use href="#s1" x="88" opacity=".4"/></g></svg></div></div>
    </div>
  </div>
</section>

<section class="section students">
  <div class="students-photo" role="img" aria-label="Photo of students studying together in a library"></div>
  <div class="heading" style="left:667px;top:68px"><span class="mark"></span><h2 style="color:#fff">Our Featured Students</h2></div>
  <p class="heading-sub" style="left:667px;top:108px;color:#fff">Vehicula ipsum sagittis vitae</p>
  <div class="student-list">
    <div class="student"><span class="avatar" role="img" aria-label="Student photo"></span><div><h5>Apiscing Eliene</h5><p>Lorem ipsum dolor sit amet, consectetur adipiscing elienean odio lorem, porta a sollicitudin velerdiet.</p></div></div>
    <div class="student"><span class="avatar" role="img" aria-label="Student photo"></span><div><h5>Soscing Mklene</h5><p>Lorem ipsum dolor sit amet, consectetur adipiscing elienean odio lorem, porta a sollicitudin velerdiet.</p></div></div>
    <div class="student"><span class="avatar" role="img" aria-label="Student photo"></span><div><h5>Biscing Ryiene</h5><p>Lorem ipsum dolor sit amet, consectetur adipiscing elienean odio lorem, porta a sollicitudin velerdiet.</p></div></div>
  </div>
  <span class="btn-yellow">VIEW MORE</span>
</section>

<section class="section courses">
  <div class="wrap">
    <div class="heading" style="top:84px"><span class="mark"></span><h2>Our Featured Coures</h2><span class="rule"></span></div>
    <p class="heading-sub" style="top:120px">vehicula ipsum sagittis vitae</p>
    <div class="course" style="left:0">
      <div class="photo" style="background:linear-gradient(135deg,#4a5c78,#8a9ab0)" role="img" aria-label="Course photo of students working at laptops"><svg width="241" height="179"><path d="M120 70v40M100 90h40" stroke="#fff" stroke-width="3"/></svg></div>
      <h4>Vivamus Porta Neque</h4><div class="meta"><span>★ 215</span><span>♥ 08</span><span class="price">$399</span></div>
    </div>
    <div class="course" style="left:263px">
      <div class="photo" style="background:linear-gradient(135deg,#c9a07c,#efe2d2)" role="img" aria-label="Course photo of a student writing notes"></div>
      <h4>Vivamus Porta Neque</h4><div class="meta"><span>★ 215</span><span>♥ 08</span><span class="price">$399</span></div>
    </div>
    <div class="course" style="left:526px">
      <div class="photo" style="background:linear-gradient(135deg,#b8c4cc,#e6e2d8)" role="img" aria-label="Course photo of two learners at a computer"></div>
      <h4>Vivamus Porta Neque</h4><div class="meta"><span>★ 215</span><span>♥ 08</span><span class="price">$399</span></div>
    </div>
    <div class="course" style="left:789px">
      <div class="photo" style="background:linear-gradient(135deg,#c58a5a,#6f8fb4)" role="img" aria-label="Course photo of a tutor with a group of children"></div>
      <h4>Vivamus Porta Neque</h4><div class="meta"><span>★ 215</span><span>♥ 08</span><span class="price">$399</span></div>
    </div>
  </div>
</section>

<section class="section counters">
  <div class="counter" style="left:85px"><b>13</b><span>Years of<br>Experiences</span></div>
  <div class="counter" style="left:363px"><b>39</b><span>Professional<br>Teacher</span></div>
  <div class="counter" style="left:616px"><b>41</b><span>News courses<br>every years</span></div>
  <div class="counter" style="left:888px"><b>97</b><span>Registered<br>Students</span></div>
</section>

<section class="section news">
  <div class="wrap">
    <div class="heading" style="top:96px"><span class="mark"></span><h2>OUR LATEST NEWS</h2><span class="rule"></span></div>
    <p class="heading-sub" style="top:132px">vehicula ipsum sagittis vitae</p>
    <div class="post" style="left:0">
      <div class="photo" style="background:linear-gradient(135deg,#d9a869,#8d6a4c)" role="img" aria-label="News photo of children reading together"><span class="date">05<br>Sep</span></div>
      <div class="by"><span>By: Lorem Ipsum</span><span>Comments: 6</span></div>
      <h4>Lorem ipsum dolor sit amet, consectetur adipiscing elit.</h4>
      <p>Lorem ipsum dolor sit amet, consectetupiscing elit. Phasellus molestie lorem vitae velit costum sapien.</p>
    </div>
    <div class="post" style="left:354px">
      <div class="photo" style="background:linear-gradient(135deg,#8fa3b8,#d6cbbb)" role="img" aria-label="News photo of a tutor with students at a table"><span class="date">012<br>Nov</span></div>
      <div class="by"><span>By: Lorem Ipsum</span><span>Comments: 6</span></div>
      <h4>Lorem ipsum dolor sit amet, consectetur adipiscing elit.</h4>
      <p>Lorem ipsum dolor sit amet, consectetupiscing elit. Phasellus molestie lorem vitae velit costum sapien.</p>
    </div>
    <div class="post" style="left:707px">
      <div class="photo" style="background:linear-gradient(135deg,#4b6a86,#b98a63)" role="img" aria-label="News photo of a smiling student in class"><span class="date">05<br>Dec</span></div>
      <div class="by"><span>By: Lorem Ipsum</span><span>Comments: 6</span></div>
      <h4>Lorem ipsum dolor sit amet, consectetur adipiscing elit.</h4>
      <p>Lorem ipsum dolor sit amet, consectetupiscing elit. Phasellus molestie lorem vitae velit costum sapien.</p>
    </div>
  </div>
</section>

<footer class="section footer">
  <div class="brand"><span class="brand-mark"></span>LendYourLessons</div>
  <p class="footer-about">Lorem ipsum dolor sit amet, consectetur adipiscing elit. Phasellus molestie lorem vitae velit consectetur male.</p>
  <div class="footer-social"><i></i><i></i><i></i></div>
  <div class="fcol" style="left:403px"><h5>Our Courses</h5><ul><li>Faster Of Taxation</li><li>Master of IT</li><li>Master Of Accounting</li><li>Biology</li><li>Chemistry</li></ul></div>
  <div class="fcol" style="left:627px"><h5>Quick Links</h5><ul><li>Home</li><li>Search</li><li>Student</li><li>Tutor</li><li>About</li><li>Contact</li></ul></div>
  <div class="fcol contact" style="left:817px;width:300px"><h5>Contact Us</h5><ul>
    <li><svg width="12" height="16" viewBox="0 0 12 16" style="flex:none;margin-top:2px"><path d="M6 0a6 6 0 016 6c0 4-6 10-6 10S0 10 0 6a6 6 0 016-6z" fill="#f7d53f"/><circle cx="6" cy="6" r="2.2" fill="#1c1c1c"/></svg>Lorem ipsum dolor sit amet, consectetur adipiscing elit. Phasellus molestie loremsapien.</li>
    <li><svg width="14" height="10" viewBox="0 0 14 10" style="flex:none;margin-top:4px"><rect width="14" height="10" fill="#f7d53f"/><path d="M0 0l7 6 7-6" stroke="#1c1c1c" fill="none"/></svg>lorem.ipsum@mailbox.example</li>
    <li><svg width="14" height="14" viewBox="0 0 12 12" style="flex:none;margin-top:2px"><path d="M2 1l3 1-1 3 3 3 3-1 1 3-2 1C5 11 1 7 1 3z" fill="#f7d53f"/></svg>+555-0199-XXXX</li>
  </ul></div>
</footer>
<div class="section base">© 2018 Lorem ipsum dolor</div>

</body>
</html>
```